Brightway Inc. Business Card Design

Brightway Inc. is in search of a great clean design for our business cards!

Looking to incorporate our full logo and watermark on side one (however, I am open to having the text and watermark separated within the design.)

On side two, I am looking to have contact information (Name, Position, Phone #, Email, Website (www.thebrightway.ca). Can have the logo and/or watermark as part of the design if applicable.

Please add tagline "Where Shine Counts" on either side 1 or 2. This tagline can be in a sans serif, serif or cursive font as long as it compliments overall design. Capitalization can be title or sentence case depending on how it fits within the design.

Get creative!! Looking for a clean, crisp, premium design! Looking for a glossy card finish with spot UV features when printed. Cards will also be printed with rounded corners. Standard dimensions (3.5 x 2).

Target Market(s)

B2B - primary clients are business owners or property management corporations. (residential jobs are few and far between)

Industry/Entity Type

Business

Contact Information for Business Card

- clean, crisp design
- double sided
- spot UV accents and glossy finish upon printing
- standard business card size (3.5 x 2) with rounded corners
- please see project description for requirements per side

Font styles to use
Sans Serif

Requirements
Must have
• - adequate bleeds with print ready files
• - cohesive design elements between side 1 & 2
• - spot UV elements (can be on both sides or just one, use your discretion)
• - colour pallet should match the logo file provided
• - incorporate tagline "where shine counts" (this tagline can be in a serif or sans serif font as long as it is complimentary to the overall design.
Nice to have
• - Premium elements with a clean design
Should not have
• - Please omit cartoon or whimsical like designs, think premium.
• - Colours should not stray from the pallet of the provided logo.

```html
<!DOCTYPE html>
<html lang="en">
<head>
<meta charset="utf-8">
<title>Brightway Inc. Business Card</title>
<link rel="stylesheet" href="https://fonts.googleapis.com/css2?family=Open+Sans:wght@400;600;700&display=swap">
<style>
  :root {
    --backdrop: #3b3431;
    --card: #141516;
    --card-edge: #1e2021;
    --teal: #2aa8a0;
    --grey: #b4b6b8;
    --white: #f2f2f2;
    --rule: #8a8d90;
  }
  * { margin: 0; padding: 0; box-sizing: border-box; }
  html, body {
    width: 1200px; height: 864px; overflow: hidden;
    background: var(--backdrop);
    font-family: "Open Sans", Arial, sans-serif;
  }
  .canvas { position: relative; width: 1200px; height: 864px; }
  .card {
    position: absolute; width: 540px; height: 309px;
    background: var(--card);
    border: 1px solid var(--card-edge);
    border-radius: 14px;
    box-shadow: 0 10px 26px rgba(0,0,0,.45);
  }
  /* Side one */
  .card-front { left: 50px; top: 150px; }
  .front-brand {
    position: absolute; left: 0; right: 0; top: 92px;
    display: flex; align-items: center; justify-content: center; gap: 14px;
  }
  .brand-square { width: 34px; height: 34px; background: var(--teal); }
  .brand-name {
    color: var(--teal); font-weight: 700; font-size: 34px; letter-spacing: .5px;
  }
  .tagline {
    position: absolute; left: 0; right: 0; top: 190px;
    display: flex; align-items: center; justify-content: center; gap: 12px;
    color: var(--grey); font-size: 15px; letter-spacing: .3px;
  }
  .tagline::before, .tagline::after {
    content: ""; width: 120px; height: 1px; background: var(--rule);
  }
  /* Side two */
  .card-back { left: 610px; top: 410px; }
  .back-brand {
    position: absolute; left: 30px; top: 130px;
    display: flex; align-items: center; gap: 9px;
  }
  .back-brand .brand-square { width: 20px; height: 20px; }
  .back-brand .brand-name { font-size: 23px; letter-spacing: 0; }
  .divider {
    position: absolute; left: 262px; top: 40px; width: 1px; height: 210px;
    background: linear-gradient(to bottom, transparent, var(--rule), transparent);
  }
  .contact { position: absolute; left: 286px; top: 56px; color: var(--white); font-size: 13.5px; line-height: 1.45; }
  .contact-name { color: var(--teal); font-weight: 700; font-size: 15px; letter-spacing: .6px; }
  .contact-role { color: var(--grey); font-size: 14px; letter-spacing: .5px; margin-bottom: 2px; }
  .contact-address { margin-bottom: 2px; }
  .contact-line { display: flex; align-items: center; gap: 8px; }
  .contact-line svg { width: 11px; height: 11px; fill: var(--teal); flex: none; }
</style>
</head>
<body>
<div class="canvas">
  <section class="card card-front" aria-label="Business card, side one">
    <div class="front-brand">
      <span class="brand-square"></span>
      <span class="brand-name">Brightway Inc.</span>
    </div>
    <p class="tagline">Where Shine Counts</p>
  </section>

  <section class="card card-back" aria-label="Business card, side two">
    <div class="back-brand">
      <span class="brand-square"></span>
      <span class="brand-name">Brightway Inc.</span>
    </div>
    <div class="divider"></div>
    <div class="contact">
      <p class="contact-name">DANIEL HART</p>
      <p class="contact-role">CEO/FOUNDER</p>
      <p class="contact-address">412 Lakeview Drive<br>Calgary, Alberta 20418</p>
      <p class="contact-line">
        <svg viewBox="0 0 12 12" aria-hidden="true"><path d="M1 3c0-1 1-2 2-2l1.5 2.5L3.5 5c.6 1.4 2 2.8 3.5 3.5l1.5-1L11 9c0 1-1 2-2 2C4.5 11 1 7.5 1 3z"/></svg>
        403 555 0182
      </p>
      <p class="contact-line">
        <svg viewBox="0 0 12 12" aria-hidden="true"><path d="M3 0h6a1 1 0 0 1 1 1v10a1 1 0 0 1-1 1H3a1 1 0 0 1-1-1V1a1 1 0 0 1 1-1zm0 2v7h6V2z"/></svg>
        403 555 0147
      </p>
      <p class="contact-line">
        <svg viewBox="0 0 12 12" aria-hidden="true"><path d="M3 0h6v4H3zM1 5h10v5H9v2H3v-2H1zm3 4v2h4V9z"/></svg>
        403 555 0199
      </p>
      <p class="contact-line">
        <svg viewBox="0 0 12 12" aria-hidden="true"><path d="M0 2h12v8H0zm1 1v.5l5 3.5 5-3.5V3z"/></svg>
        info@thebrightway.ca
      </p>
      <p class="contact-line">
        <svg viewBox="0 0 12 12" aria-hidden="true"><circle cx="6" cy="6" r="6"/><circle cx="6" cy="6" r="2" fill="#141516"/></svg>
        www.thebrightway.ca
      </p>
    </div>
  </section>
</div>
</body>
</html>
```